CBD PATCHES

Design creation of my CBD patch box.
Product must look Pharamaceutical grade.
Colours need to look pharmaceutical (green/white/maybe a bit of blue).
Text: Cannabidiol (CBD) Self-curing adhesive Polyethylene backing sheet.
Apply one patch to a smooth are of skin. Each patch can be worn for up to 24 hours. Apply subsequent patches to different areas to allow the skin to breathe between uses.
Do not apply to broken or irritable skin. Consult a doctor if you are taking medications or have medical conditions before using this or any other supplement. Do not use if you are pregnant or breastfeeding.
Store in a cool, dry place out of direct sunlight. Stable for three years. Once opened, use within 12 months.

```html
<!DOCTYPE html>
<html lang="en">
<head>
<meta charset="utf-8">
<title>Verdacare CBD Patch Box – Dieline</title>
<link rel="stylesheet" href="https://fonts.googleapis.com/css2?family=Roboto:wght@400;700&family=Roboto+Condensed:wght@700&display=swap">
<style>
  :root {
    --ink: #0d3a45;
    --dieline: #d9d9d9;
    --paper: #ffffff;
    --leaf: #8fe879;
    --leaf-soft: #c9f5c0;
    --mint: #6fe3c6;
    --aqua: #2fd3e8;
    --teal: #1fb0c4;
    --brand: #c6f3a6;
    --badge: #1d2b33;
  }
  * { margin: 0; padding: 0; box-sizing: border-box; }
  html, body { width: 1200px; height: 900px; overflow: hidden; background: var(--paper); }
  .canvas { position: relative; width: 1200px; height: 900px; font-family: "Roboto", Arial, sans-serif; color: var(--ink); }
  .artwork { position: absolute; inset: 0; }
  .text { position: absolute; }

  .directions {
    left: 272px; top: 314px; width: 209px;
    transform: rotate(180deg);
    font-size: 7.6px; line-height: 10.3px; text-align: justify;
  }
  .directions p + p { margin-top: 10px; }
  .directions .warning-strong { font-weight: 700; }

  .brand-name {
    left: 241px; top: 523px; width: 120px; text-align: center;
    font-weight: 700; font-size: 10.5px; letter-spacing: 0.4px; color: var(--brand);
  }

  .product-title { left: 258px; top: 613px; }
  .product-title h1 {
    font-family: "Roboto Condensed", "Arial Narrow", sans-serif;
    font-size: 23px; line-height: 24px; font-weight: 700;
  }
  .product-title .spec { font-size: 13px; line-height: 15.5px; }
  .dose-pill {
    left: 244px; top: 670px; width: 133px; height: 12px;
    background: var(--ink); color: #fff; border-radius: 0 6px 6px 0;
    font-size: 8.4px; line-height: 12px; padding-left: 14px;
  }
  .dose-pill b { font-weight: 700; }

  .claims {
    left: 244px; top: 750px; width: 258px; text-align: center;
    font-size: 8.8px; font-weight: 700; letter-spacing: 0.1px;
  }
  .claims span { margin: 0 4px; }

  .range-callout {
    left: 698px; top: 146px; width: 270px; text-align: center;
    font-size: 13px; line-height: 13.5px;
  }
  .range-callout b { font-weight: 700; }

  .product-info { left: 721px; top: 246px; width: 209px; font-size: 8.4px; line-height: 10.3px; text-align: justify; }
  .product-info h2 { font-size: 8.6px; font-weight: 700; line-height: 10.3px; }
  .product-info p + h2 { margin-top: 10px; }

  .reorder { left: 698px; top: 566px; width: 250px; text-align: center; }
  .reorder h2 {
    font-family: "Roboto Condensed", "Arial Narrow", sans-serif;
    font-size: 22px; line-height: 22px; font-weight: 700;
  }
  .reorder p { font-size: 8.6px; margin-top: 5px; }
</style>
</head>
<body>
<div class="canvas">
  <svg class="artwork" width="1200" height="900" viewBox="0 0 1200 900" xmlns="http://www.w3.org/2000/svg">
    <defs>
      <linearGradient id="leafToAqua" x1="0" y1="0" x2="1" y2="0.2">
        <stop offset="0" stop-color="#a6ee8e"/>
        <stop offset="0.55" stop-color="#3fd0b8"/>
        <stop offset="1" stop-color="#52e0ea"/>
      </linearGradient>
      <linearGradient id="aquaDown" x1="0" y1="0" x2="0" y2="1">
        <stop offset="0" stop-color="#34d6ea"/>
        <stop offset="0.5" stop-color="#5fe0cc"/>
        <stop offset="1" stop-color="#a7efa0"/>
      </linearGradient>
      <linearGradient id="leafWash" x1="0" y1="0" x2="1" y2="1">
        <stop offset="0" stop-color="#d6f8cd"/>
        <stop offset="0.6" stop-color="#9ceb88"/>
        <stop offset="1" stop-color="#b9f1ae"/>
      </linearGradient>
      <linearGradient id="infoWave" x1="0" y1="0" x2="0" y2="1">
        <stop offset="0" stop-color="#c5f4b8"/>
        <stop offset="0.5" stop-color="#5fdcc2"/>
        <stop offset="1" stop-color="#22cbe6"/>
      </linearGradient>
      <clipPath id="leftTopPanel"><rect x="244" y="179" width="258" height="256"/></clipPath>
      <clipPath id="frontPanel"><rect x="244" y="435" width="258" height="268"/></clipPath>
      <clipPath id="bottomPanel"><rect x="244" y="703" width="258" height="107"/></clipPath>
      <clipPath id="rightTopPanel"><rect x="698" y="101" width="259" height="107"/></clipPath>
      <clipPath id="infoPanel"><rect x="698" y="208" width="259" height="267"/></clipPath>
      <clipPath id="backPanel"><rect x="698" y="475" width="259" height="257"/></clipPath>
    </defs>

    <!-- left carton dieline -->
    <g class="dieline" fill="none" stroke="var(--dieline)" stroke-width="1.3">
      <path d="M244,179 C262,175 269,160 269,140 L269,62 L335,62 C345,86 357,97 373,97 C389,97 401,86 410,62 L477,62 L477,140 C477,160 484,175 502,179"/>
      <path d="M244,187 L151,187 L151,315 C151,380 190,420 244,425"/>
      <path d="M502,188 L595,188 L595,315 C595,380 556,420 502,425"/>
      <path d="M327,810 C331,834 350,848 373,848 C396,848 415,834 420,810"/>
      <rect x="244" y="179" width="258" height="631"/>
      <line x1="244" y1="435" x2="502" y2="435"/>
      <line x1="244" y1="703" x2="502" y2="703"/>
    </g>

    <!-- left carton artwork -->
    <g clip-path="url(#leftTopPanel)">
      <path d="M244,179 L452,179 C420,235 370,255 355,280 C345,330 340,380 300,412 C280,428 260,432 244,440 Z" fill="url(#leafToAqua)" opacity="0.9"/>
      <path d="M244,179 L410,179 C380,225 340,240 315,275 C295,305 280,360 244,400 Z" fill="#a8ef96" opacity="0.55"/>
    </g>
    <g clip-path="url(#frontPanel)">
      <path d="M244,435 L305,435 C285,455 265,470 244,485 Z" fill="#7fe0b0" opacity="0.8"/>
      <path d="M502,435 C485,470 465,495 455,520 C440,560 450,580 420,600 C380,630 350,660 325,703 L502,703 Z" fill="url(#aquaDown)"/>
      <path d="M502,540 C470,570 430,600 400,640 C380,665 350,685 330,703 L502,703 Z" fill="#b3f1b8" opacity="0.55"/>
      <circle cx="468" cy="478" r="18" fill="var(--badge)"/>
      <circle cx="466" cy="659" r="25" fill="#fff"/>
      <circle cx="466" cy="659" r="25" fill="none" stroke="var(--ink)" stroke-width="1"/>
      <circle cx="301" cy="488" r="31" fill="var(--brand)"/>
    </g>
    <g clip-path="url(#bottomPanel)">
      <path d="M330,703 L502,703 L502,810 L330,810 C322,780 320,735 330,703 Z" fill="url(#leafWash)"/>
    </g>

    <!-- right carton dieline -->
    <g class="dieline" fill="none" stroke="var(--dieline)" stroke-width="1.3">
      <path d="M781,101 C785,80 800,64 827,64 C854,64 869,80 874,101"/>
      <path d="M698,485 C645,490 606,540 606,600 L606,723 L698,723"/>
      <path d="M957,485 C1010,490 1049,540 1049,600 L1049,723 L957,723"/>
      <path d="M698,732 C715,740 723,755 723,780 L723,849 L790,849 C797,830 810,815 827,815 C844,815 858,830 866,849 L931,849 L931,780 C931,755 940,740 957,732"/>
      <rect x="698" y="101" width="259" height="631"/>
      <line x1="698" y1="208" x2="957" y2="208"/>
      <line x1="698" y1="475" x2="957" y2="475"/>
    </g>

    <!-- right carton artwork -->
    <g clip-path="url(#rightTopPanel)">
      <path d="M698,101 L870,101 C878,140 880,180 876,208 L698,208 Z" fill="url(#leafWash)"/>
    </g>
    <g clip-path="url(#infoPanel)">
      <path d="M698,208 L876,208 C872,250 850,280 815,320 C775,360 745,410 698,475 Z" fill="url(#infoWave)"/>
      <path d="M698,208 L820,208 C800,250 770,280 740,330 C720,365 710,400 698,430 Z" fill="#b7f1a9" opacity="0.5"/>
    </g>
    <g clip-path="url(#backPanel)">
      <path d="M957,505 C935,540 925,590 915,650 C905,690 860,710 832,732 L957,732 Z" fill="url(#aquaDown)" opacity="0.85"/>
      <path d="M957,600 C920,630 880,680 850,732 L957,732 Z" fill="#b6f1a8" opacity="0.7"/>
    </g>
  </svg>

  <div class="text directions">
    <p>Apply one patch to a smooth are of skin. Each patch can be worn for up to 24 hours. Apply subsequent patches to different areas to allow the skin to breathe between uses.</p>
    <p>Do not apply to broken or irritable skin. Consult a doctor if you are taking medications or have medical conditions before using this or any other supplement. <span class="warning-strong">Do not use if you are pregnant or breastfeeding.</span></p>
  </div>

  <div class="text brand-name">VERDACARE</div>

  <div class="text product-title">
    <h1>Cannabidiol</h1>
    <p class="spec">Self-curing Adhesive</p>
    <p class="spec">Polyethylene Backing Sheet</p>
  </div>
  <div class="text dose-pill"><b>20mg</b> CBD Isolate Per Patch</div>

  <div class="text claims">VEGAN<span>·</span>THC FREE<span>·</span>100% CANNABIDIOL</div>

  <div class="text range-callout">DISCOVER THE RANGE AT<br><b>www.website.com</b></div>

  <div class="text product-info">
    <h2>STORAGE</h2>
    <p>Store in a cool, dry place out of direct sunlight. Stable for three years. Once opened, use within 12 months.</p>
    <h2>INGREDIENTS</h2>
    <p>Lorem ipsum dolor sit amet, consectetur adipiscing elit. Mauris vel lorem sit amet diam efficitur vehicula. Suspendisse vel diam et tellus consequat sagittis dictum sed nunc. Quisque dui velit, posuere vel odio ac, efficitur placerat tellus. Nam efficitur purus vitae dui consequat consectetur. Nullam at est euismod, rutrum tortor a, tincidunt purus. Donec pharetra fermentum diam vitae porta. Quisque elementum, odio sit amet lobortis commodo, enim velit suscipit erat, ac ornare sem sapien et diam. Donec a diam vitae nulla imperdiet rutrum. Vestibulum sed urna sapien. Sed eleifend ultricies ex at venenatis. Maecenas elementum feugiat iaculis.</p>
  </div>

  <div class="text reorder">
    <h2>YOU’VE<br>RUN OUT!</h2>
    <p>Find more at www.website.com</p>
  </div>
</div>
</body>
</html>
```